Tovalmer's 50th Anniversary Gala

Need a cool invitation to be printed on #120 paper for a nonprofit gala fundraiser. Verbiage for invitation is below. Event logo is attached. Could potentially use black and gold but NOT a requirement. Want it to be FUN and DIFFERENT.

Colors
0054AA
0677BA
7BADD7
CADEEF
E8F1F8

```html
<!DOCTYPE html>
<html lang="en">
<head>
<meta charset="utf-8">
<title>Tovalmer's 50th Anniversary Gala – Invitation</title>
<link rel="stylesheet" href="https://fonts.googleapis.com/css2?family=Montserrat:wght@400;700&family=Great+Vibes&display=swap">
<style>
  :root {
    --page-bg: #e9eaec;
    --card-bg: #040607;
    --gold: #e9cf86;
    --gold-light: #f6e6a8;
    --gold-deep: #b98a2e;
    --confetti-top: #7a5a1a;
  }
  * { box-sizing: border-box; margin: 0; padding: 0; }
  html, body {
    width: 1200px; height: 1200px; overflow: hidden;
    background: var(--page-bg);
    font-family: "Montserrat", Arial, sans-serif;
  }
  .invitation {
    position: absolute; left: 205px; top: 55px;
    width: 790px; height: 1090px;
    background: var(--card-bg);
    color: var(--gold);
  }
  .confetti-band {
    position: absolute; left: 0; top: 0; width: 100%; height: 268px;
    background: linear-gradient(180deg, var(--confetti-top) 0%, rgba(122,90,26,0.35) 55%, rgba(4,6,7,0) 100%);
  }
  .line-item {
    position: absolute; left: 0; width: 100%;
    text-align: center; transform: translateY(-50%);
    white-space: nowrap; line-height: 1.2;
  }
  .intro { top: 273px; font-size: 24px; }
  .event-name {
    top: 374px; font-size: 40px; font-weight: 700;
    letter-spacing: 1px; color: var(--gold);
    display: flex; justify-content: center; align-items: center; gap: 14px;
  }
  .event-name .mark {
    width: 16px; height: 16px; border-radius: 50%; background: var(--gold);
  }
  .title {
    top: 517px; font-family: "Great Vibes", cursive; font-size: 118px;
    background: linear-gradient(90deg, var(--gold-deep), var(--gold-light) 45%, var(--gold-deep));
    -webkit-background-clip: text; background-clip: text; color: transparent;
    padding: 0 20px;
  }
  .rule {
    position: absolute; left: 50%; height: 2px; background: var(--gold);
    transform: translateX(-50%);
  }
  .rule--wide { width: 263px; }
  .rule--top { top: 608px; }
  .rule--bottom { top: 675px; }
  .rule--short { width: 84px; top: 986px; }
  .date { top: 641px; font-size: 32px; font-weight: 700; color: var(--gold-light); }
  .date sup { font-size: 18px; }
  .time { top: 712px; font-size: 25px; }
  .venue { top: 785px; font-size: 25px; }
  .address { top: 827px; font-size: 25px; }
  .offer {
    top: 886px; font-size: 25px;
    display: flex; justify-content: center; align-items: center; gap: 28px;
  }
  .offer svg { width: 24px; height: 24px; fill: var(--gold); }
  .dress { top: 946px; font-size: 25px; }
  .ticket-note { top: 1027px; font-size: 21px; }
</style>
</head>
<body>
  <main class="invitation">
    <div class="confetti-band" role="img" aria-label="Scattered gold confetti and sparkles across the top of the card"></div>

    <p class="line-item intro">Join us for a memorable night!</p>

    <div class="line-item event-name"><span class="mark"></span>Tovalmer</div>

    <h1 class="line-item title">Gala Celebration</h1>

    <div class="rule rule--wide rule--top"></div>
    <p class="line-item date">Friday, November 8<sup>th</sup></p>
    <div class="rule rule--wide rule--bottom"></div>

    <p class="line-item time">6:30 – 10 p.m.</p>
    <p class="line-item venue">The Marlowe</p>
    <p class="line-item address">2145 Linden Park Avenue</p>

    <p class="line-item offer">
      <svg viewBox="0 0 24 24" aria-hidden="true"><polygon points="12,1 15,9 23.5,9 16.6,14 19.2,22.5 12,17.3 4.8,22.5 7.4,14 0.5,9 9,9"/></svg>
      <span>Hors d’oeuvres and Cocktails</span>
      <svg viewBox="0 0 24 24" aria-hidden="true"><polygon points="12,1 15,9 23.5,9 16.6,14 19.2,22.5 12,17.3 4.8,22.5 7.4,14 0.5,9 9,9"/></svg>
    </p>

    <p class="line-item dress">Semi-formal</p>
    <div class="rule rule--short"></div>
    <p class="line-item ticket-note">Ticket information on reverse</p>
  </main>
</body>
</html>
```